Erklär-Flyer für Gutschein-Ankauf-Service Bonkarten-Profi.de
Zielgruppe
Auf http://www.bonkarten-profi.de/ bieten wir u.a. den Service an, ungenutzte Geschenkkarten von großen Händlern wie z.B. Technoplatz, Vandoro, WOLM, usw. direkt gegen Bargeld einzutauschen. Diesen Service wollen wir nun in einem Flyer vorstellen.
Die Zielgruppe des zu erstellenden Flyers sollen vor allem Mitarbeiter bei Firmen z.B. Auto Verkäufer sein, die von Ihrem Arbeitgeber als Prämie Geschenkgutscheine als Incentive erhalten und diese aber lieber in Bargeld umtauschen würden.
Das Wunschszenario wäre: Wir schicken den Flyer zusammen mit einem Anschreiben an die jeweiligen Firmen. Der/diejenige die den Brief und Flyer entgegennimmt, erkennt den Sinn und Nutzen und gibt den Flyer an Ihre Kollegen weiter bzw. hängt ihn ans schwarze Brett etc.
Aufgabenstellung
Gestaltet werden soll ein 3 Schritte Falz-Flyer (z.B. 6-seitiger Altarfalz Fensterfalz) angelehnt an das bisherige Design auf Bonkarten-Profi.de (nicht zwingend 100%, gerne auch eigene Ideen). Auf der Außenseite nur kurz in einem Satz um was es geht und auf der Innenseite dann am Besten in 3 Schritten erklärt, wie einfach der Umtausch von Gutscheinen in Bargeld ist.
Das Wichtigste ist die "Bequemlichkeit, Einfachheit, kein Aufwand", am zweitwichtigsten ist "Sicherheit, Seriosität" (Unsere Seite gibt es schon seit 2008 und wir wurden bereits im KRT vorgestellt).
Verteilung des Falt-Flyer als Brief mit der Post. Wenn der Brief geöffnet wird ist der zu erreichende Optimal Zustand, dass der Flyer von der Person, die den Brief öffnet, z.B. ans "schwarze Brett" gehängt wird als Info bzw. eine Art Anleitung.

```html
<!DOCTYPE html>
<html lang="de">
<head>
<meta charset="utf-8">
<title>Bonkarten-Profi.de – Falz-Flyer</title>
<link href="https://fonts.googleapis.com/css2?family=Open+Sans:wght@300;400;600;700&display=swap" rel="stylesheet">
<style>
  :root {
    --blue: #2c63a8;
    --blue-dark: #1f4f95;
    --blue-soft: #5b87c0;
    --green: #a3c423;
    --green-dark: #8fb01a;
    --sky: #dbe9f6;
    --sky-light: #eef5fb;
    --ink: #333a44;
    --white: #ffffff;
    --line: #9aa3ad;
  }
  * { box-sizing: border-box; margin: 0; padding: 0; }
  html, body { width: 851px; height: 1200px; overflow: hidden; }
  body {
    position: relative;
    background: var(--white);
    font-family: "Open Sans", Arial, sans-serif;
    color: var(--ink);
  }

  /* ---------- Cover ---------- */
  .cover {
    position: absolute; left: 230px; top: 26px; width: 397px; height: 560px;
    overflow: hidden;
  }
  .cover-photo {
    position: absolute; inset: 0;
    background:
      radial-gradient(ellipse at 68% 28%, #efe2d2 0%, #d9c2a6 22%, transparent 45%),
      radial-gradient(ellipse at 70% 75%, #8b6a4f 0%, transparent 45%),
      linear-gradient(160deg, #eaf1f7 0%, #c9d7e4 45%, #9fb2c4 100%);
  }
  .cover-brand {
    position: absolute; left: 18px; top: 34px;
    font-size: 22px; font-weight: 700; color: var(--blue);
    letter-spacing: -0.3px;
  }
  .claim-badge {
    position: absolute; left: -8px; top: 120px; width: 100px; height: 100px;
    border-radius: 50%; background: var(--green);
    display: flex; align-items: center; padding-left: 26px;
    color: var(--white); font-size: 15px; font-weight: 300; line-height: 1.25;
  }
  .headline-box {
    position: absolute; left: 214px; top: 392px; width: 159px; height: 104px;
    background: rgba(255,255,255,0.82);
    text-align: right; padding: 8px 10px 0 0;
  }
  .headline-box .lead { color: var(--blue-soft); font-size: 14px; font-weight: 400; line-height: 1.2; display: block; text-align: left; padding-left: 10px; }
  .headline-box .main { color: var(--blue-dark); font-size: 21px; font-weight: 700; line-height: 1.2; display: block; margin-top: 8px; }
  .media-badge {
    position: absolute; left: 311px; top: 342px; width: 84px; height: 84px;
    border-radius: 50%; background: var(--green);
    display: flex; flex-direction: column; align-items: center; justify-content: center;
    color: var(--white); font-size: 11px; line-height: 1.25; text-align: center;
  }
  .media-badge b { font-weight: 700; }

  /* ---------- Inside ---------- */
  .inside {
    position: absolute; left: 37px; top: 615px; width: 786px; height: 560px;
    overflow: hidden;
    background: linear-gradient(180deg, var(--sky) 0%, var(--sky-light) 55%, var(--sky) 100%);
  }
  .advantage-seal {
    position: absolute; left: 229px; top: -70px; width: 160px; height: 160px;
    border-radius: 50%; background: var(--blue-dark); color: var(--white);
    text-align: center; padding-top: 82px; line-height: 1.15;
  }
  .advantage-seal .small { font-size: 13px; font-weight: 300; display: block; }
  .advantage-seal .big { font-size: 19px; font-weight: 600; display: block; }
  .intro-box {
    position: absolute; left: 342px; top: 61px; width: 215px; height: 89px;
    background: rgba(255,255,255,0.85); padding: 8px 10px;
    font-size: 10px; line-height: 1.45; color: var(--blue); text-align: justify;
  }
  .intro-box b { font-weight: 700; }
  .inside-brand {
    position: absolute; left: 672px; top: 28px;
    font-size: 15px; font-weight: 700; color: var(--blue);
  }

  .panel { position: absolute; top: 183px; height: 222px; background: var(--white); }
  .panel-select { left: 0; width: 170px; clip-path: polygon(0 0, 150px 0, 170px 50%, 150px 100%, 0 100%); padding: 22px 0 0 4px; }
  .panel-register { left: 165px; width: 400px; clip-path: polygon(0 0, 380px 0, 400px 50%, 380px 100%, 0 100%, 20px 50%); padding: 6px 0 0 10px; }
  .panel-payout { left: 560px; width: 226px; clip-path: polygon(0 0, 226px 0, 226px 100%, 0 100%, 20px 50%); }
  .payout-photo {
    position: absolute; inset: 0;
    background: radial-gradient(ellipse at 55% 45%, #caa283 0%, #6b4a3a 40%, #f1f4f7 75%);
  }

  .step-title { font-size: 8px; font-weight: 700; color: #111; border-bottom: 1px solid #111; width: 140px; padding-bottom: 1px; }
  .step-title span { background: #111; color: var(--white); padding: 0 3px; margin-right: 3px; }
  .step-sub { font-size: 4.5px; color: #555; margin: 4px 0 8px; }
  .shop-list { display: grid; grid-template-columns: repeat(3, 48px); row-gap: 7px; font-size: 4.6px; color: #333; list-style: none; }
  .shop-list li::before { content: "➜ "; color: var(--blue); }

  .choice { font-size: 7.5px; font-weight: 600; color: #222; display: flex; align-items: center; gap: 4px; margin-left: 8px; height: 11px; }
  .choice i { width: 7px; height: 7px; border-radius: 50%; border: 1px solid var(--line); display: inline-block; }
  .choice i.on { background: radial-gradient(circle, #333 35%, #fff 45%); }
  .field { display: flex; align-items: center; height: 17px; font-size: 7.5px; font-weight: 600; color: #222; margin-left: 12px; }
  .field label { width: 174px; }
  .field .box { width: 88px; height: 10px; border: 1px solid var(--line); background: var(--white); }
  .field .box.active { border-color: #8fb6dd; }
  .field .box + .box { margin-left: 21px; }
  .field.first { margin-top: 8px; }
  .payout-note { font-size: 7.5px; color: #222; border-top: 1px solid #ccc; margin: 10px 0 0 0; padding-top: 4px; width: 380px; }

  .frames { position: absolute; left: 0; top: 0; width: 786px; height: 560px; pointer-events: none; }

  .step-num {
    position: absolute; width: 62px; height: 62px; border-radius: 50%;
    background: var(--green); border: 3px solid var(--white);
    color: var(--white); font-size: 36px; font-weight: 700;
    display: flex; align-items: center; justify-content: center;
  }
  .num-1 { left: 86px; top: 139px; }
  .num-2 { left: 274px; top: 394px; }
  .num-3 { left: 609px; top: 139px; }

  .caption { position: absolute; top: 428px; font-size: 10px; line-height: 1.45; color: var(--blue); }
  .caption b { font-weight: 700; }
  .cap-1 { left: 18px; width: 160px; }
  .cap-2 { left: 345px; width: 200px; }
  .cap-3 { left: 604px; width: 170px; }
</style>
</head>
<body>

<section class="cover">
  <div class="cover-photo" role="img" aria-label="Foto: lächelnde Frau mit Einkaufstüten über der Schulter"></div>
  <div class="cover-brand">Bonkarten-Profi.de</div>
  <div class="claim-badge">einfach.<br>schnell.<br>seriös.</div>
  <div class="headline-box">
    <span class="lead">Machen Sie<br>ungenutze</span>
    <span class="main">Gutscheine<br>zu Geld</span>
  </div>
  <div class="media-badge">Bekannt aus<br>dem <b>KRT</b></div>
</section>

<section class="inside">
  <div class="advantage-seal"><span class="small">Unser Vorteil ist</span><span class="big">Ihr Vorteil!</span></div>
  <div class="intro-box">Mit unserem <b>Ankaufspreis-Rechner</b> sehen sie sofort wie viel Sie für Ihren Gutschein bekommen und können diesen per <b>Sofortverkauf</b> in eine neue Form der Kaufkraft umwandeln.*</div>
  <div class="inside-brand">Bonkarten-Profi.de</div>

  <div class="panel panel-select">
    <div class="step-title"><span>1</span>Anbieter auswählen</div>
    <div class="step-sub">Drücken Sie auf einen der folgenden Anbieter</div>
    <ul class="shop-list">
      <li>Vandoro</li><li>Technoplatz</li><li>Lindera</li>
      <li>WOLM</li><li>Kaufeck</li><li>Morvia</li>
      <li>Brisant</li><li>Fotowerk</li><li>Tessano</li>
      <li>Luvio</li><li>Buchhain</li><li>Pradel</li>
      <li>Schuhwelt</li><li>Nordmann</li><li>Kelvo</li>
      <li>Sportal</li><li>Modehaus</li><li>Trendo</li>
      <li>Gartenzeit</li><li>Spielfeld</li><li>Oriam</li>
      <li>Reisewelt</li><li>Duftland</li><li>Velora</li>
    </ul>
  </div>

  <div class="panel panel-register">
    <div class="choice"><i></i>Ja, ich habe bereits ein Konto und möchte mich einloggen.</div>
    <div class="choice"><i class="on"></i>Ich bin ein neuer Kunde und möchte meine Daten nun eingeben.</div>
    <div class="field first"><label>E-Mailadresse</label><span class="box"></span></div>
    <div class="field"><label>Passwort wählen</label><span class="box"></span></div>
    <div class="field"><label>Passwort bestätigen (erneut)</label><span class="box"></span></div>
    <div class="field"><label>Vorname</label><span class="box"></span></div>
    <div class="field"><label>Nachname</label><span class="box"></span></div>
    <div class="field"><label>Straße und Hausnr.</label><span class="box active"></span></div>
    <div class="field"><label>PLZ und Ort</label><span class="box"></span><span class="box"></span></div>
    <div class="field"><label>Ihre Telefonnummer</label><span class="box"></span></div>
    <div class="payout-note">Wir zahlen Ihr Guthaben nach Erhalt des Gutscheins innerhalb von einer Woche auf Ihr Konto aus.</div>
  </div>

  <div class="panel panel-payout">
    <div class="payout-photo" role="img" aria-label="Foto: junge Frau hält Geldscheine in der Hand"></div>
  </div>

  <svg class="frames" viewBox="0 0 786 560" aria-hidden="true">
    <g fill="none" stroke="var(--green)" stroke-width="3">
      <polygon points="0,183 150,183 170,294 150,405 0,405"/>
      <polygon points="165,183 545,183 565,294 545,405 165,405 185,294"/>
      <polygon points="560,183 786,183 786,405 560,405 580,294"/>
    </g>
  </svg>

  <div class="step-num num-1">1</div>
  <div class="step-num num-2">2</div>
  <div class="step-num num-3">3</div>

  <p class="caption cap-1">Wählen Sie auf Unserer Website <b>www.bonkarten-profi.de</b> Ihren Geschenkanbieter aus.</p>
  <p class="caption cap-2">Melden Sie sich <b>kostenlos</b> an und geben Sie Ihre Gutschein-Informationen ein</p>
  <p class="caption cap-3">Ausdrucken und den Gutschein an uns senden. Das Geld erhalten Sie <b>direkt auf ihr Konto.</b></p>
</section>

</body>
</html>
```